Design the Mobile Version of Existing Web Based Health Platform

Loomcrest is a social business enterprise that focus on public health by applying innovative healthcare services and consumer internet technology. Loomcrest offers a personalized platform of health promotion and disease prevention that puts the individual back in control of his life.

Loomcrest is looking for a Mobile Web UX/Visual Design professional to create a mobile version of Loomcrest website platform for iPhone, iPad/tablet and Android.

Contestants must to check www.loomcrest-demo.com.br to have a better understanding of Loomcrest Platform by creating an account (it's in portuguese, but anyone can get the general idea).

The mobile version of Loomcrest should have very similar functionality and user flows. This job is not to reengineer or re-imagine Loomcrest. It is just to reformat the existing functionality so it works well on mobile devices.

This description below is to help you to understand the core features of the platform (check the attachments to see the new web design of each one):

- Personally Controlled Health Record - PCHR enables an individual to own and manage a complete, secure, digital copy of her health and wellness information.
- Health Risk Assessments - is a process to estimate the nature and probability of adverse health effects, based on personal and family historical data, behavior and environment.
- Simulation of future health - "what if analysis" that emphasizes health education and behavior change.
- Step Quests - a program that gives you the opportunity to the participant to advance his personal well-being by doing simple Step Quests
- Health Alerts and Recommendations and Missing Data - Recommendations based on Wellbeing Bureau Guidelines and Federal Wellness Review Panel (FWRP), plus notifications to update outdated information.

The deliverable for this project is a psd file with a designed mobile version of Loomcrest.

A new design of the web platform is under construction. You can also check it looking at the files attached.

Target Market(s)

people 25-40 years old, 60% female, socially engaged

Industry/Entity Type

Healthcare

Requirements
Must have
• iPhone, iPad and Android version

Design must cover all current functionalities available on the web version (please, ensure you understand all features by creating an account at www.loomcrest-demo.com.br)

- Login/Sign up
- Welcome (first assessment)
- Add to Personal Controlled Health Record (PCHR)
- Update/Remove PCHR
- List PCHR
- Riskgrid (risk assessmen results)
- Simulation
- Alerts
- Missing data
- Recommendations
- StepQuest
- Badges
- Configurations

It's important to check the attachments to see how the web platform design is evolving.

```html
<!DOCTYPE html>
<html lang="en">
<head>
<meta charset="utf-8">
<title>Loomcrest – Personal Health Record</title>
<link rel="stylesheet" href="https://fonts.googleapis.com/css2?family=Arimo:wght@400;700&family=Roboto+Condensed:wght@300;400&display=swap">
<style>
  :root{
    --page-bg:#ececec;
    --green:#9ccc3c;
    --green-dark:#88b52f;
    --orange:#f26c0f;
    --orange-light:#f7892e;
    --band-top:#e8e8e8;
    --band-bottom:#dcdcdc;
    --content-bg:#f5f5f5;
    --card-bg:#fafafa;
    --line:#dedede;
    --title:#555555;
    --text:#7a7a7a;
    --edit-bg:#5b5b5b;
    --white:#ffffff;
  }
  *{box-sizing:border-box;margin:0;padding:0}
  html,body{width:864px;height:1200px;overflow:hidden;background:var(--page-bg)}
  .screen{
    position:absolute;left:96px;top:0;width:672px;height:1200px;
    background:var(--content-bg);overflow:hidden;
    font-family:"Roboto Condensed",sans-serif;
  }
  .topbar{
    position:absolute;left:0;top:0;width:100%;height:86px;
    background:var(--green);border-bottom:2px solid var(--green-dark);
  }
  .brand{position:absolute;left:30px;top:22px;display:flex;align-items:center;gap:14px}
  .brand-mark{width:48px;height:48px;background:var(--white);border-radius:3px}
  .brand-name{font-family:"Arimo",sans-serif;font-weight:700;font-size:26px;color:var(--white)}
  .menu-btn{
    position:absolute;right:22px;top:22px;width:55px;height:44px;
    background:var(--white);border-radius:4px;
    display:flex;flex-direction:column;justify-content:center;align-items:center;gap:5px;
  }
  .menu-btn span{display:block;width:33px;height:4px;background:var(--orange);border-radius:1px}
  .toolbar{
    position:absolute;left:0;top:86px;width:100%;height:211px;
    background:linear-gradient(var(--band-top),var(--band-bottom));
    border-bottom:1px solid var(--line);
  }
  .page-title{
    position:absolute;top:32px;width:100%;text-align:center;
    font-family:"Arimo",sans-serif;font-weight:700;font-size:37px;color:var(--title);
  }
  .filter{
    position:absolute;top:107px;height:58px;background:var(--white);
    border:1px solid #cfcfcf;font-size:19px;font-weight:300;color:var(--text);
    padding-left:22px;line-height:56px;
  }
  .filter.recent{left:35px;width:207px}
  .filter.category{left:255px;width:207px}
  .add-btn{
    position:absolute;top:107px;left:476px;width:162px;height:58px;
    background:linear-gradient(var(--orange-light),var(--orange));
    color:var(--white);font-family:"Arimo",sans-serif;font-weight:700;font-size:22px;
    text-align:center;line-height:58px;
  }
  .section-head{position:absolute;left:36px;display:flex;align-items:center;gap:16px}
  .section-head h2{font-family:"Arimo",sans-serif;font-weight:700;font-size:37px;color:var(--green)}
  .measures-head{top:340px}
  .lifestyle-head{top:644px}
  .record-list{
    position:absolute;left:35px;width:604px;background:var(--card-bg);
    border:1px solid var(--line);list-style:none;
  }
  .measures{top:425px}
  .lifestyle{top:718px}
  .record{position:relative;height:86px;border-top:1px solid var(--line);font-size:19px;font-weight:300;color:var(--text)}
  .record:first-child{border-top:none}
  .record > *{position:absolute;top:50%;transform:translateY(-50%)}
  .rec-icon{left:16px;width:36px;height:36px}
  .rec-label{left:87px}
  .rec-value{left:240px}
  .rec-date{right:80px;font-size:18px}
  .edit-btn{right:16px;width:42px;height:42px;background:var(--edit-bg);border-radius:2px;display:flex;align-items:center;justify-content:center}
</style>
</head>
<body>
<main class="screen">
  <header class="topbar">
    <div class="brand"><span class="brand-mark"></span><span class="brand-name">Loomcrest</span></div>
    <div class="menu-btn" aria-label="Menu"><span></span><span></span><span></span></div>
  </header>

  <section class="toolbar">
    <h1 class="page-title">Personal Health Record</h1>
    <div class="filter recent">Mais Recentes</div>
    <div class="filter category">Todas Categories</div>
    <div class="add-btn">Adicioner</div>
  </section>

  <div class="section-head measures-head">
    <svg width="38" height="38" viewBox="0 0 38 38" fill="none" stroke="#f26c0f" stroke-width="2.5"><circle cx="17" cy="17" r="13"/><circle cx="17" cy="17" r="4"/><path d="M17 30 H35"/></svg>
    <h2>Medidas</h2>
  </div>
  <ul class="record-list measures">
    <li class="record">
      <svg class="rec-icon" viewBox="0 0 36 36"><rect x="3" y="6" width="30" height="28" rx="5" fill="#f26c0f"/><circle cx="18" cy="11" r="7" fill="#fff"/><circle cx="18" cy="11" r="4" fill="#f26c0f"/></svg>
      <span class="rec-label">Weight</span><span class="rec-value">50kg</span><span class="rec-date">20 Aug,2013</span>
      <span class="edit-btn"><svg width="24" height="24" viewBox="0 0 24 24" fill="none" stroke="#fff" stroke-width="2"><path d="M4 20 L6 14 L17 3 L21 7 L10 18 Z M4 20 L10 18"/></svg></span>
    </li>
    <li class="record">
      <svg class="rec-icon" viewBox="0 0 36 36" fill="#f26c0f"><rect x="3" y="2" width="7" height="32"/><circle cx="23" cy="6" r="4"/><rect x="18" y="11" width="10" height="12" rx="2"/><rect x="19" y="22" width="3" height="12"/><rect x="24" y="22" width="3" height="12"/></svg>
      <span class="rec-label">Height</span><span class="rec-value">60cm</span><span class="rec-date">20 Aug,2013</span>
      <span class="edit-btn"><svg width="24" height="24" viewBox="0 0 24 24" fill="none" stroke="#fff" stroke-width="2"><path d="M4 20 L6 14 L17 3 L21 7 L10 18 Z M4 20 L10 18"/></svg></span>
    </li>
  </ul>

  <div class="section-head lifestyle-head">
    <svg width="40" height="40" viewBox="0 0 40 40" fill="none" stroke="#f26c0f" stroke-width="2.5"><rect x="8" y="10" width="24" height="16" rx="4" transform="rotate(-40 20 18)"/><path d="M14 14 L24 26"/></svg>
    <h2>Estilo de vida</h2>
  </div>
  <ul class="record-list lifestyle">
    <li class="record">
      <svg class="rec-icon" viewBox="0 0 36 36" fill="#f26c0f"><rect x="1" y="24" width="34" height="7"/><rect x="22" y="8" width="3" height="14"/><rect x="27" y="4" width="3" height="18"/></svg>
      <span class="rec-label">Smoke</span><span class="rec-value">No</span><span class="rec-date">20 Aug,2013</span>
      <span class="edit-btn"><svg width="24" height="24" viewBox="0 0 24 24" fill="none" stroke="#fff" stroke-width="2"><path d="M4 20 L6 14 L17 3 L21 7 L10 18 Z M4 20 L10 18"/></svg></span>
    </li>
    <li class="record">
      <svg class="rec-icon" viewBox="0 0 36 36" fill="#f26c0f"><circle cx="16" cy="6" r="4"/><path d="M8 24 Q10 12 18 12 L26 18 L22 20 L18 17 L16 24 Z"/><rect x="4" y="27" width="28" height="2"/><rect x="8" y="32" width="20" height="2"/></svg>
      <span class="rec-label">Physical Activity</span><span class="rec-value">1 per week</span><span class="rec-date">20 Aug,2013</span>
      <span class="edit-btn"><svg width="24" height="24" viewBox="0 0 24 24" fill="none" stroke="#fff" stroke-width="2"><path d="M4 20 L6 14 L17 3 L21 7 L10 18 Z M4 20 L10 18"/></svg></span>
    </li>
    <li class="record">
      <svg class="rec-icon" viewBox="0 0 36 36" fill="#f26c0f"><path d="M18 32 L4 18 A8 8 0 0 1 18 8 A8 8 0 0 1 32 18 Z"/></svg>
      <span class="rec-label">Heart beat</span><span class="rec-value">Normal</span><span class="rec-date">20 Aug,2013</span>
      <span class="edit-btn"><svg width="24" height="24" viewBox="0 0 24 24" fill="none" stroke="#fff" stroke-width="2"><path d="M4 20 L6 14 L17 3 L21 7 L10 18 Z M4 20 L10 18"/></svg></span>
    </li>
  </ul>
</main>
</body>
</html>
```